An anniversary gift for my girlfriend

My girlfriend and I have been dating for almost 2 years. We met online and this has afforded us the really unique opportunity to have the first words we said to each other (the whole conversation, in fact) preserved. We're moving in together in a few months and she doesn't know that I saved the conversation. I've been waiting for this to turn it into something we can hang in our new place.

The only phrase I want to use is:
"Well if you dislike people's knees then I think we'll get along famously"

It's an Nobody Leaves Before Midnight in Portland reference for the curious.

I want the poster to use the words themselves as the art; I'm thinking typography. I'd like it to match her aesthetic, she likes to wear Nora Vell and T. Brisk. Colors shouldn't be anything too "girly". Somewhere I'd like to include the date June 1, 2015. It shouldn't be a major piece of the poster though, just a way to denote the date.

It should fit (and be fully visible in) a 16x20 (inches) frame

Thanks in advance for the work!

Requirements
Must have
• Must use only the words: "Well if you dislike people's knees then I think we'll get along famously"
• I want this to be typography, so making the phrase the center of the poster and the art itself.

```html
<!DOCTYPE html>
<html lang="en">
<head>
<meta charset="utf-8">
<title>Famously — Anniversary Poster</title>
<link href="https://fonts.googleapis.com/css2?family=Abril+Fatface&family=Playfair+Display:ital,wght@1,400&family=Raleway:wght@300;400&display=swap" rel="stylesheet">
<style>
  :root {
    --poster-bg: #465f6c;
    --ink: #ffffff;
  }
  * { margin: 0; padding: 0; box-sizing: border-box; }
  html, body {
    width: 1200px;
    height: 863px;
    overflow: hidden;
    background: var(--poster-bg);
  }
  .poster {
    position: relative;
    width: 1200px;
    height: 863px;
    background: var(--poster-bg);
    color: var(--ink);
  }
  .quote-line { position: absolute; white-space: nowrap; line-height: 1; }
  .open-mark {
    left: 296px; top: 212px;
    font-family: "Abril Fatface", serif;
    font-size: 104px;
  }
  .lead-in {
    left: 362px; top: 222px;
    font-family: "Playfair Display", serif;
    font-style: italic;
    font-size: 52px;
  }
  .key-word { font-family: "Abril Fatface", serif; }
  .dislike { left: 380px; top: 280px; font-size: 122px; }
  .knees {
    left: 330px; top: 412px;
    font-family: "Raleway", sans-serif;
    font-weight: 300;
    font-size: 70px;
    letter-spacing: -1px;
  }
  .bridge {
    left: 392px; top: 486px;
    font-family: "Playfair Display", serif;
    font-style: italic;
    font-size: 38px;
  }
  .close-mark {
    left: 872px; top: 446px;
    font-family: "Abril Fatface", serif;
    font-size: 128px;
  }
  .famously { left: 334px; top: 510px; font-size: 124px; }
  .accent-dot {
    position: absolute;
    left: 810px; top: 300px;
    width: 96px; height: 96px;
    border-radius: 50%;
    background: var(--ink);
  }
  .date-stamp {
    position: absolute;
    left: 306px; top: 688px;
    display: flex; align-items: center; gap: 6px;
    font-family: "Raleway", sans-serif;
    font-weight: 400;
    font-size: 28px;
  }
  .home-icon { width: 26px; height: 24px; }
</style>
</head>
<body>
<main class="poster">
  <span class="quote-line open-mark">&ldquo;</span>
  <span class="quote-line lead-in">Well if you</span>
  <span class="quote-line key-word dislike">dislike</span>
  <span class="accent-dot" aria-hidden="true"></span>
  <span class="quote-line knees">people&rsquo;s knees</span>
  <span class="quote-line bridge">then I think we&rsquo;ll get along</span>
  <span class="quote-line close-mark">&rdquo;</span>
  <span class="quote-line key-word famously">famously</span>
  <p class="date-stamp">
    June 1, 2015.
    <svg class="home-icon" viewBox="0 0 32 30" aria-hidden="true">
      <path d="M16 2 L31 15 H26 V28 H19 V20 H13 V28 H6 V15 H1 Z" fill="var(--ink)"/>
    </svg>
  </p>
</main>
</body>
</html>
```